Ashcombe Heritage Guild Harvest Lantern Days Event Flyer - Historic Event

I need a flyer about the Ashcombe Heritage Guild's Harvest Lantern Days event October 8th and 9th. The centerpiece of Harvest Lantern Days is Civil War reenactments. I want the flyer to include the schedule of events and be eye catching on area bulletin boards. Our website is www.ashcombeheritageguild.org for more information and pictures. The website for the Calder Ridge Rangers reenactors is http://www.calderridgerangers.com/.

Target Market(s)

Our target market is middle ages (35-70) families and couples. Most are history buffs, especially about the Civil War.

Industry/Entity Type

Non-Profit

Font styles to use
Serif
Decorative
Script

Requirements
Must have
• The flyer must include the majority of the schedule attached - especially the battle times, museums, and anything including food.The dance on Saturday night is also important. The bottom of the flyer MUST say "Paid in part by Quillan County Visitor Levy Board"
Nice to have
• Pictures

```html
<!DOCTYPE html>
<html lang="en">
<head>
<meta charset="utf-8">
<title>Ashcombe Heritage Guild – Historic Event 2016</title>
<link rel="stylesheet" href="https://fonts.googleapis.com/css2?family=Bebas+Neue&family=Lato:ital,wght@0,400;0,700;1,400;1,700&family=Marcellus&family=Roboto+Condensed:ital,wght@1,700&display=swap">
<style>
  :root {
    --paper: #f7f3ee;
    --ink: #1f1a17;
    --title-red: #6e1d0c;
    --accent-red: #8a1f0f;
    --gold: #e7b72a;
    --gold-light: #f3cf55;
    --band-dark: #4e150a;
    --band: #7a2a12;
    --rule: #d8cfc6;
    --white: #ffffff;
  }
  * { margin: 0; padding: 0; box-sizing: border-box; }
  html, body { width: 869px; height: 1200px; overflow: hidden; background: var(--paper); }
  .flyer { position: relative; width: 869px; height: 1200px; background: var(--paper); overflow: hidden; font-family: "Lato", sans-serif; color: var(--ink); }

  .hero-photo {
    position: absolute; left: 0; top: 0; width: 869px; height: 380px;
    background: linear-gradient(180deg, #3b3b3b 0%, #6d6d6d 35%, #9a9a9a 62%, rgba(247,243,238,0) 100%);
  }

  .title {
    position: absolute; top: 326px; left: 0; width: 100%; text-align: center;
    font-family: "Bebas Neue", sans-serif; font-size: 76px; letter-spacing: 1px;
    color: var(--title-red); line-height: 1;
  }

  .event-pill {
    position: absolute; left: 152px; top: 427px; width: 566px; height: 65px;
    border-radius: 12px; background: linear-gradient(180deg, var(--gold-light), var(--gold));
    box-shadow: 0 6px 10px rgba(0,0,0,0.15);
    font-family: "Marcellus", serif; font-size: 50px; line-height: 65px; text-align: center; color: var(--ink);
  }

  .dates {
    position: absolute; top: 518px; left: 0; width: 100%; text-align: center;
    font-family: "Bebas Neue", sans-serif; font-size: 36px; color: var(--accent-red);
  }
  .dates span { font-family: "Lato", sans-serif; font-size: 18px; color: var(--ink); margin-left: 6px; }

  .divider { position: absolute; left: 416px; top: 585px; width: 1px; height: 445px; background: var(--rule); }

  .day { position: absolute; }
  .day--saturday { left: 41px; top: 592px; width: 360px; }
  .day--sunday { left: 524px; top: 604px; width: 290px; }
  .day h2 { font-family: "Bebas Neue", sans-serif; font-weight: 400; font-size: 34px; line-height: 1; margin-bottom: 12px; color: var(--ink); }

  .schedule { list-style: none; }
  .schedule li { display: flex; font-size: 12.5px; line-height: 15.5px; margin-bottom: 5.5px; }
  .schedule .time { flex: 0 0 68px; font-family: "Marcellus", serif; font-size: 12px; color: var(--accent-red); }
  .day--sunday .schedule .time { flex: 0 0 60px; color: var(--ink); }
  .schedule .what { font-style: italic; }

  .highlights { position: absolute; left: 527px; top: 780px; list-style: none; }
  .highlights li {
    font-family: "Roboto Condensed", sans-serif; font-style: italic; font-weight: 700;
    font-size: 21px; line-height: 31px; color: var(--accent-red);
  }
  .highlights li::before { content: "•"; font-style: normal; color: var(--ink); margin-right: 8px; }

  .footer-band { position: absolute; left: 0; top: 935px; width: 869px; height: 265px; }

  .sponsor { position: absolute; left: 24px; top: 1050px; color: var(--white); }
  .sponsor .paid { font-family: "Bebas Neue", sans-serif; font-size: 33px; color: var(--gold); line-height: 1; }
  .sponsor .board { font-family: "Marcellus", serif; font-size: 30px; line-height: 1.3; }
  .sponsor .guild { font-family: "Lato", sans-serif; font-size: 23px; margin-top: 8px; }

  .contact { position: absolute; left: 393px; top: 1106px; list-style: none; color: var(--white); font-size: 13.5px; }
  .contact li { display: flex; align-items: center; gap: 6px; margin-bottom: 26px; }

  .call-badge {
    position: absolute; left: 666px; top: 968px; width: 186px; height: 186px; border-radius: 50%;
    background: #111; border: 9px solid var(--gold);
    display: flex; flex-direction: column; align-items: center; justify-content: center; text-align: center;
  }
  .call-badge .label { font-family: "Bebas Neue", sans-serif; font-size: 36px; color: var(--gold); line-height: 1; }
  .call-badge .phone { font-family: "Bebas Neue", sans-serif; font-size: 30px; color: var(--white); line-height: 1.1; letter-spacing: 0.5px; }
</style>
</head>
<body>
<main class="flyer">
  <div class="hero-photo" role="img" aria-label="Black and white photograph of Civil War reenactors marching down a country trail"></div>

  <h1 class="title">Ashcombe Heritage Guild</h1>
  <div class="event-pill">Historic Event-2016</div>
  <p class="dates">8th and 9th October <span>(Saturday and sunday)</span></p>

  <div class="divider"></div>

  <section class="day day--saturday">
    <h2>8th Oct,Saturday, 2016</h2>
    <ul class="schedule">
      <li><span class="time"></span><span class="what">Through the Day –<br>Demonstrations and Speakers in<br>various locations</span></li>
      <li><span class="time">10:00 AM</span><span class="what">Battle by Calder Ridge Rangers<br>Sponsored in part by Hollis's<br>General Stores</span></li>
      <li><span class="time">11:30-1:00</span><span class="what">Chicken Biscuit Bake at Town Hall<br>Free Will Donation</span></li>
      <li><span class="time"></span><span class="what">Afternoon – Trolley and Buggy Rides</span></li>
      <li><span class="time">1:00-4:00</span><span class="what">Museums Opens</span></li>
      <li><span class="time">1:30-2:00</span><span class="what">Birthday Cake on Marlow House Front Porch</span></li>
      <li><span class="time"></span><span class="what">Cake donated by Greenway - Quarry City</span></li>
      <li><span class="time">2:00</span><span class="what">Battle by Calder Ridge Rangers</span></li>
      <li><span class="time">3:00</span><span class="what">Sightseeing Cruise on the Spirit of Ashcombe</span></li>
      <li><span class="time">6:00</span><span class="what">Dance at Town Hall with Lanternlight Band</span></li>
    </ul>
  </section>

  <section class="day day--sunday">
    <h2>9th Oct,Sunday, 2016</h2>
    <ul class="schedule">
      <li><span class="time">12:30</span><span class="what">PM Parade on Main Street</span></li>
      <li><span class="time"></span><span class="what">Afternoon – Buggy &amp; Trolley Rides</span></li>
      <li><span class="time">1:00-4:00</span><span class="what">Museums Open</span></li>
      <li><span class="time">1:30</span><span class="what">Battle by Calder Ridge Rangers</span></li>
      <li><span class="time">2:00</span><span class="what">Pie Reception at Ashcombe Depot and<br>Railroad History Museum</span></li>
      <li><span class="time">3:00</span><span class="what">Sightseeing Cruise</span></li>
    </ul>
  </section>

  <ul class="highlights">
    <li>Especially the battle times</li>
    <li>Museums</li>
    <li>Anything including food</li>
  </ul>

  <svg class="footer-band" viewBox="0 0 869 265" preserveAspectRatio="none" aria-hidden="true">
    <defs>
      <linearGradient id="bandFill" x1="0" y1="0" x2="1" y2="0">
        <stop offset="0" stop-color="#4e150a"/>
        <stop offset="1" stop-color="#7a2a12"/>
      </linearGradient>
    </defs>
    <path d="M0 30 L20 22 L38 30 L60 20 L85 28 L110 18 L140 30 L170 24 L200 34 L235 26 L265 36 L300 30 L330 42 L360 34 L395 40 L420 28 L445 30 L470 46 L500 42 L530 50 L560 44 L590 52 L620 38 L650 48 L690 40 L730 44 L780 36 L830 40 L869 34 L869 265 L0 265 Z" fill="url(#bandFill)"/>
    <path d="M0 30 L20 22 L38 30 L60 20 L85 28 L110 18 L140 30 L170 24 L200 34 L235 26 L265 36 L300 30 L330 42 L360 34 L395 40 L420 28 L445 30 L470 46 L500 42 L530 50 L560 44 L590 52 L620 38 L650 48" fill="none" stroke="#e7b72a" stroke-width="2.5"/>
  </svg>

  <div class="sponsor">
    <p class="paid">Paid in part by Quillan County</p>
    <p class="board">Visitor Levy Board</p>
    <p class="guild">Ashcombe Heritage Guild</p>
  </div>

  <ul class="contact">
    <li>
      <svg width="13" height="10" viewBox="0 0 13 10" aria-hidden="true"><rect x="0.5" y="0.5" width="12" height="9" fill="none" stroke="#e7b72a"/><path d="M0.5 0.5 L6.5 5.5 L12.5 0.5" fill="none" stroke="#e7b72a"/></svg>
      hello@ashcombeheritageguild.org
    </li>
    <li>
      <svg width="10" height="10" viewBox="0 0 10 10" aria-hidden="true"><circle cx="5" cy="5" r="4.5" fill="#e7b72a"/></svg>
      www.ashcombeheritageguild.org
    </li>
  </ul>

  <div class="call-badge">
    <span class="label">Call Us</span>
    <span class="phone">(555)314-2790</span>
  </div>
</main>
</body>
</html>
```